Autohaus sucht Visitenkarten
Zielgruppe
Verkauf und Reparatur von PKW
Zielgruppe ist jeder Autofahrer/in
Aufgabenstellung
Erstellen eines Visitenkartendesigns mit stilisiertem Auto als Logo, eher modern gestaltet, ohne Schnörkel, zweifarbig, Anthrazit sollte im Logo enthalten sein.

```html
<!DOCTYPE html>
<html lang="de">
<head>
<meta charset="utf-8">
<title>Autohaus Brenner – Visitenkarten</title>
<link href="https://fonts.googleapis.com/css2?family=Roboto+Condensed:wght@300;400;700&display=swap" rel="stylesheet">
<style>
  :root {
    --anthracite: #474747;
    --anthracite-dark: #3c3c3c;
    --brand-blue: #009fe3;
    --paper: #ffffff;
    --ink: #1e1e1e;
    --backdrop: #c6c6c6;
    --font-main: "Roboto Condensed", "Arial Narrow", sans-serif;
  }
  * { box-sizing: border-box; margin: 0; padding: 0; }
  html, body { width: 1200px; height: 963px; overflow: hidden; }
  body {
    position: relative;
    font-family: var(--font-main);
    background: var(--backdrop);
  }

  .card {
    position: absolute;
    width: 600px; height: 372px;
    overflow: hidden;
  }

  .wordmark {
    font-family: var(--font-main);
    font-weight: 400;
    text-transform: uppercase;
    letter-spacing: -0.5px;
    white-space: nowrap;
  }

  /* Front */
  .card--front { left: 70px; top: 60px; background: var(--paper); }
  .card__header {
    position: absolute; left: 0; top: 0; width: 100%; height: 106px;
    background: var(--anthracite);
    border-bottom: 8px solid var(--brand-blue);
  }
  .card__header .wordmark {
    position: absolute; right: 30px; top: 46px;
    font-size: 32px; color: var(--paper);
  }
  .card__footer-band {
    position: absolute; left: 0; bottom: 0; width: 100%; height: 22px;
    background: var(--brand-blue);
  }
  .person { position: absolute; left: 50px; top: 134px; }
  .person__name {
    font-size: 23px; font-weight: 400; color: var(--brand-blue);
    text-transform: uppercase;
  }
  .person__role { font-size: 16px; font-weight: 300; color: var(--ink); margin-top: 2px; }

  .contact {
    position: absolute;
    font-size: 15.5px; font-weight: 300; color: var(--ink);
    line-height: 27px;
  }
  .contact--personal { left: 50px; top: 222px; }
  .contact--company { left: 345px; top: 150px; }
  .contact__row { display: flex; white-space: nowrap; }
  .contact__label { width: 56px; }
  .contact__web { color: var(--brand-blue); font-weight: 400; }

  /* Back */
  .card--back { left: 530px; top: 470px; background: var(--anthracite); }
  .card--back .wordmark {
    position: absolute; left: 0; right: 0; top: 112px;
    text-align: center; font-size: 56px; color: var(--paper);
  }
  .card--back .card__web {
    position: absolute; left: 0; right: 0; top: 272px;
    text-align: center; font-size: 17px; font-weight: 300; color: var(--paper);
  }
  .card--back .card__stripe {
    position: absolute; left: 0; top: 334px; width: 100%; height: 14px;
    background: var(--brand-blue);
  }

  .presentation-mark {
    position: absolute; left: 76px; top: 800px;
    font-size: 44px; color: var(--anthracite);
  }
</style>
</head>
<body>
  <section class="card card--front" aria-label="Visitenkarte Vorderseite">
    <div class="card__header">
      <span class="wordmark">Autohaus Brenner</span>
    </div>
    <div class="person">
      <div class="person__name">Jonas Feldmann</div>
      <div class="person__role">Verkauf</div>
    </div>
    <div class="contact contact--personal">
      <div class="contact__row"><span class="contact__label">Telefon</span><span>0987 | 61 42 30-10</span></div>
      <div class="contact__row"><span class="contact__label">Telefax</span><span>0987 | 61 42 39-11</span></div>
      <div class="contact__row"><span class="contact__label">Email</span><span>jfe@autohausbrenner.de</span></div>
    </div>
    <div class="contact contact--company">
      <div class="contact__row">Lindenweg 10</div>
      <div class="contact__row">54321 Talstadt</div>
      <div class="contact__row"><span class="contact__label">Telefon</span><span>0987 | 61 42 30-0</span></div>
      <div class="contact__row"><span class="contact__label">Telefax</span><span>0987 | 61 42 39-1</span></div>
      <div class="contact__row"><span class="contact__label">Email</span><span>info@autohausbrenner.de</span></div>
      <div class="contact__row contact__web">www.autohausbrenner.de</div>
    </div>
    <div class="card__footer-band"></div>
  </section>

  <section class="card card--back" aria-label="Visitenkarte Rückseite">
    <span class="wordmark">Autohaus Brenner</span>
    <div class="card__web">www.autohausbrenner.de</div>
    <div class="card__stripe"></div>
  </section>

  <div class="wordmark presentation-mark">Autohaus Brenner</div>
</body>
</html>
```